Email Signatures

I would like to create a new email signature for my team. The design will be the same for everyone, with only individual details such as name and email changing. You can also see our brand style on our website. https://www.tlmbespokehomes.com.au/

Target Market(s)

Clients for new builds or renovations

Industry/Entity Type

Construction

Colors

Designer to choose colors to be used in the design.

```html
<!DOCTYPE html>
<html lang="en">
<head>
<meta charset="utf-8">
<title>TLM Email Signature</title>
<link href="https://fonts.googleapis.com/css2?family=Exo+2:wght@400;700&display=swap" rel="stylesheet">
<style>
  :root {
    --page-bg: #ebebeb;
    --card-bg: #ffffff;
    --brand-green: #10813f;
    --bright-green: #2fa84a;
    --charcoal: #312d2c;
    --steel-light: #c9c9c9;
    --steel-dark: #5a5a5a;
    --text-light: #ffffff;
    --logo-ink: #2b2b2b;
  }
  html, body {
    margin: 0;
    width: 1200px;
    height: 1200px;
    overflow: hidden;
    background: var(--page-bg);
  }
  .canvas {
    width: 1200px;
    height: 1200px;
    display: flex;
    align-items: center;
    justify-content: center;
  }
  .signature {
    display: block;
    width: 1025px;
    height: 235px;
    font-family: "Exo 2", sans-serif;
  }
  .brand-name { fill: var(--logo-ink); font-weight: 700; font-size: 64px; letter-spacing: 2px; }
  .person-name { fill: var(--text-light); font-weight: 700; font-size: 16px; letter-spacing: 0.6px; }
  .person-role { fill: var(--text-light); font-weight: 400; font-size: 14px; }
  .contact-line { fill: var(--text-light); font-weight: 400; font-size: 12.5px; letter-spacing: 0.3px; }
  .contact-icon { fill: var(--text-light); }
</style>
</head>
<body>
<main class="canvas">
  <svg class="signature" viewBox="0 0 820 188" xmlns="http://www.w3.org/2000/svg" aria-label="TLM email signature">
    <defs>
      <linearGradient id="steel" x1="0" y1="1" x2="1" y2="0">
        <stop offset="0" stop-color="var(--steel-dark)"/>
        <stop offset="0.5" stop-color="var(--steel-light)"/>
        <stop offset="1" stop-color="var(--steel-dark)"/>
      </linearGradient>
    </defs>

    <rect class="card" width="820" height="188" fill="var(--card-bg)"/>

    <!-- brand name -->
    <text class="brand-name" x="168" y="118" text-anchor="middle">TLM</text>

    <!-- green header wedge -->
    <polygon class="header-band" points="308,0 820,0 820,73 450,73 393,140" fill="var(--brand-green)"/>

    <!-- steel bevel and dark contact panel -->
    <polygon class="bevel" points="343,188 448,78 472,78 372,188" fill="url(#steel)"/>
    <polygon class="contact-panel" points="452,78 820,78 820,188 380,188" fill="var(--charcoal)"/>
    <line class="accent-stripe" x1="388" y1="188" x2="490" y2="80" stroke="var(--bright-green)" stroke-width="2.5"/>

    <!-- name and role -->
    <text class="person-name" x="494" y="34">LIAM PORTER</text>
    <text class="person-role" x="494" y="53">General Manager</text>

    <!-- contact icons -->
    <path class="contact-icon" d="M494,99 q1,-1 2,0 l1.5,2 q0.5,1 -0.5,1.5 q1,2.5 3,3.5 q0.5,-1 1.5,-0.5 l2,1.5 q0.5,1 -0.5,2 q-2,1.5 -5,-1 q-3,-3 -4,-5.5 q-1,-2.5 0,-3.5z"/>
    <rect class="contact-icon" x="494" y="119" width="8" height="6" rx="0.8"/>
    <path d="M494.5,119.5 l3.5,3 l3.5,-3" fill="none" stroke="var(--charcoal)" stroke-width="0.9"/>
    <circle cx="498" cy="140" r="4" fill="none" stroke="var(--text-light)" stroke-width="1.2"/>
    <path d="M494,140 h8 M498,136 v8" stroke="var(--text-light)" stroke-width="0.8"/>
    <path class="contact-icon" d="M498,155 a3.5,3.5 0 0 1 3.5,3.5 q0,2.5 -3.5,6.5 q-3.5,-4 -3.5,-6.5 a3.5,3.5 0 0 1 3.5,-3.5z"/>
    <circle cx="498" cy="158.5" r="1.3" fill="var(--charcoal)"/>

    <!-- contact details -->
    <text class="contact-line" x="508" y="107">0400 123 456</text>
    <text class="contact-line" x="508" y="126">info@tlmbespokehomes.com.au</text>
    <text class="contact-line" x="508" y="145">www.tlmbespokehomes.com.au</text>
    <text class="contact-line" x="508" y="164">Devonport, Tasmania, Australia</text>
  </svg>
</main>
</body>
</html>
```